DORLIT HOMES Professional Home Buyers

Please see two files uploaded. One is my new LOGO (thanks Quenby) and the other gives the wording and pages desired. Of course I am open to suggestions to further enhance what I'm about. I don't want testimonials or houses to buy to appear but to have room for them when I'm ready. I am a real estate investor not a licensed real estate agent. For FAQ i want just the questions to appear and when they click on the question the answer appears and when they click on the question again the answer disappears. make sense? When you read my wording and my idea of pages you'll get an idea of what I'm about. Suggestions are welcomed.

Industry/Entity Type

Real Estate

Number of Pages Required

5+ page

Requirements
Must have
• FAQ pages only questions appear. They click on question the answer appears underneath. they click on question again, the answer disappears. Also, I of course, want my new LOGO to appear on each page I don't know if it will look better all by itself or blended in somehow? Call now 418-555-0193 on each page also. I will get a real phone number before website goes live. If you have a better way of wording what I'm describing please let me know, I am open to feedback
Nice to have
• Anything that the average homeowner can relate to (yea I know, that doesn't help you much, right?)
• Testimonial page and houses to buy page could be done with just the shell ready in the wings for when my business grows it will be ready all that it would need then are the wording and pictures to be uploaded onto the website page. make sense?
Should not have
• I don't want it too elegant or rich looking as I believe my audience will be mostly the average homeowner who needs help

```html
<!DOCTYPE html>
<html lang="en">
<head>
<meta charset="utf-8">
<title>DORLIT HOMES – Professional Home Buyers</title>
<link href="https://fonts.googleapis.com/css2?family=Lato:wght@400;700;900&family=Open+Sans:wght@400;600;700&display=swap" rel="stylesheet">
<style>
:root{
  --page:#eef0f2;
  --white:#ffffff;
  --ink:#2b3440;
  --muted:#6b7380;
  --navy:#1d2a38;
  --blue:#2a78c2;
  --blue-dark:#1e5f9a;
  --card-blue:#1f618f;
  --card-orange:#e39d27;
  --card-red:#d4553a;
  --footer:#22262c;
  --footer-deep:#181b20;
  --line:#d3d8de;
}
*{box-sizing:border-box;margin:0;padding:0}
html,body{width:1200px;height:2256px;overflow:hidden}
body{background:var(--page);font-family:"Open Sans",Arial,sans-serif;color:var(--ink)}
.site{width:1200px;height:2256px;position:relative}
.wrap{width:984px;margin:0 auto}

/* top bar */
.topbar{height:32px;background:var(--navy);color:#c8d1db;font-size:11px}
.topbar .wrap{display:flex;justify-content:space-between;align-items:center;height:32px}
.topbar .call{font-weight:700;color:#fff;letter-spacing:.5px}

/* header */
.header{height:64px;background:var(--white)}
.header .wrap{display:flex;justify-content:space-between;align-items:center;height:64px}
.brand{display:flex;align-items:center;gap:10px}
.brand-dot{width:14px;height:14px;border-radius:50%;background:var(--blue)}
.brand-name{font-family:"Lato",sans-serif;font-weight:900;font-size:20px;color:var(--navy);letter-spacing:1px}
.nav{display:flex;gap:6px;list-style:none}
.nav li{font-family:"Lato",sans-serif;font-size:12px;font-weight:700;color:var(--ink);padding:8px 16px;letter-spacing:.5px}
.nav li.active{background:var(--blue);color:#fff}

/* hero */
.hero{height:504px;position:relative;color:#fff;text-align:center;overflow:hidden}
.hero-photo{position:absolute;inset:0;background:linear-gradient(180deg,#6f9fd0 0%,#9ec1e2 35%,#7d8c99 70%,#3e4a55 100%)}
.hero-content{position:relative;padding-top:150px}
.hero h1{font-family:"Lato",sans-serif;font-weight:900;font-size:40px;letter-spacing:1px;text-shadow:0 2px 6px rgba(0,0,0,.35)}
.hero p{font-size:15px;font-weight:600;line-height:1.6;margin:22px auto 0;width:520px;text-shadow:0 1px 4px rgba(0,0,0,.4)}
.btn{display:inline-block;background:var(--blue);color:#fff;font-family:"Lato",sans-serif;font-weight:700;font-size:14px;letter-spacing:1px;padding:14px 30px}
.hero .btn{margin-top:34px}

/* about */
.about{height:340px;background:var(--white);text-align:center;padding-top:40px}
.mark{width:16px;height:16px;border-radius:50%;background:var(--navy);margin:0 auto 10px}
.section-title{font-family:"Lato",sans-serif;font-weight:700;font-size:34px;color:var(--blue-dark);letter-spacing:1px}
.about h3{font-family:"Lato",sans-serif;font-weight:400;font-size:22px;color:var(--blue-dark);margin-top:14px;letter-spacing:.5px}
.about p{font-size:12px;color:var(--muted);line-height:1.7;width:720px;margin:18px auto 0}
.about .btn{margin-top:26px}

/* services */
.services{height:480px;margin-top:20px;position:relative;overflow:hidden}
.services-photo{position:absolute;inset:0;background:linear-gradient(180deg,#6e8599 0%,#506273 50%,#36424e 100%)}
.services-inner{position:relative;padding-top:36px;text-align:center}
.services .section-title{color:#fff;border-bottom:1px solid rgba(255,255,255,.5);display:inline-block;padding:0 20px 6px;font-weight:400}
.cards{display:flex;justify-content:center;gap:44px;margin-top:48px}
.card{width:292px;height:300px;color:#fff;text-align:left;padding:26px 28px;border:4px solid rgba(255,255,255,.85)}
.card.home{background:var(--card-blue)}
.card.sale{background:var(--card-orange)}
.card.invest{background:var(--card-red)}
.card-head{display:flex;align-items:center;gap:16px;padding-bottom:18px;border-bottom:1px solid rgba(255,255,255,.6)}
.card-head h4{font-family:"Lato",sans-serif;font-weight:700;font-size:24px;letter-spacing:.5px}
.card ul{list-style:none;margin-top:20px}
.card li{font-size:12.5px;font-weight:600;line-height:1.45;margin-bottom:16px;padding-left:22px;position:relative}
.card li::before{content:"";position:absolute;left:0;top:4px;width:9px;height:9px;border-radius:50%;background:#fff}

/* contact */
.contact{height:480px;background:var(--white);text-align:center;padding-top:38px}
.contact .sub{font-size:11px;color:var(--muted);margin-top:6px}
.form{display:flex;justify-content:center;gap:24px;margin-top:44px;text-align:left}
.form .col{display:flex;flex-direction:column;gap:16px}
.field{width:330px;height:44px;border:1px solid var(--line);display:flex;align-items:center;gap:10px;padding:0 12px;font-size:11px;color:#9aa1aa}
.field.message{height:164px;align-items:flex-start;padding-top:14px}
.ico{width:14px;height:14px;border-radius:2px;background:#b9c0c8;flex:none}
.contact .btn{margin-top:30px;padding:12px 48px}

/* footer */
.footer{height:248px;background:var(--footer);margin-top:20px;color:#c3c8cf}
.footer .wrap{display:flex;gap:0;padding-top:36px}
.fcol{width:246px}
.fcol h5{font-family:"Lato",sans-serif;font-weight:700;font-size:14px;color:#fff;letter-spacing:.5px;margin-bottom:14px}
.fcol ul{list-style:none}
.fcol li{font-size:11px;line-height:1.9;padding-left:14px;position:relative}
.fcol li::before{content:"›";position:absolute;left:0;color:#fff}
.fcol p{font-size:11px;line-height:1.7}
.social{display:flex;gap:8px;margin-top:8px}
.social span{width:22px;height:22px;border-radius:50%;background:#8d96a1}
.nl-input{width:190px;height:24px;background:#fff;margin-top:8px;font-size:10px;color:#9aa1aa;padding:5px 8px}
.nl-btn{display:inline-block;margin-top:10px;background:#fff;color:var(--ink);font-weight:700;font-size:10px;padding:5px 12px}
.copyright{height:48px;background:var(--footer-deep);color:#9aa2ac;font-size:10px;text-align:center;line-height:48px}
</style>
</head>
<body>
<div class="site">
  <div class="topbar">
    <div class="wrap">
      <span>Professional Home Buyers Serving Your Neighborhood</span>
      <span class="call">CALL NOW: 418-555-0193</span>
    </div>
  </div>

  <header class="header">
    <div class="wrap">
      <div class="brand"><span class="brand-dot"></span><span class="brand-name">DORLIT HOMES</span></div>
      <ul class="nav">
        <li class="active">HOME</li><li>ABOUT US</li><li>FAQ</li><li>CONTACT US</li><li>TESTIMONIALS</li><li>HOUSES TO BUY</li>
      </ul>
    </div>
  </header>

  <section class="hero wrap">
    <div class="hero-photo" role="img" aria-label="City skyline with tall residential towers under a blue sky"></div>
    <div class="hero-content">
      <h1>LOREM IPSUM IS SIMPLY</h1>
      <p>LOREM IPSUM IS SIMPLY DUMMY TEXT OF THE PRINTING AND TYPESETTING LOREM IPSUM IS SIMPLY</p>
      <span class="btn">READ MORE</span>
    </div>
  </section>

  <section class="about wrap">
    <div class="mark"></div>
    <h2 class="section-title">ABOUT US</h2>
    <h3>WE BUY HOUSES IN ANY CONDITION!</h3>
    <p>DORLIT HOMES is a local investor that buys houses throughout the area. We buy houses "as is", so you don't need to repair or clean anything. Contact us today for your free, no-obligation quote.</p>
    <span class="btn">GET YOUR FREE QUOTE</span>
  </section>

  <section class="services wrap">
    <div class="services-photo" role="img" aria-label="Blurred city buildings background"></div>
    <div class="services-inner">
      <h2 class="section-title">SERVICES</h2>
      <div class="cards">
        <div class="card home">
          <div class="card-head">
            <svg width="34" height="30" viewBox="0 0 34 30"><path d="M17 2 2 15h4v13h8v-8h6v8h8V15h4z" fill="#fff"/></svg>
            <h4>HOME</h4>
          </div>
          <ul><li>WE BUY "AS IS"</li><li>NO WAITING FOR BANK LOAN APPROVALS</li><li>QUICK CLOSINGS</li></ul>
        </div>
        <div class="card sale">
          <div class="card-head">
            <svg width="34" height="30" viewBox="0 0 34 30"><path d="M3 3h14l14 14-12 11L3 14z" fill="#fff"/><circle cx="10" cy="10" r="3" fill="#e39d27"/></svg>
            <h4>SALE</h4>
          </div>
          <ul><li>WE PAY MOST CLOSING COSTS</li><li>WE BUY "AS IS"</li><li>WE PAY ALL CASH</li></ul>
        </div>
        <div class="card invest">
          <div class="card-head">
            <svg width="30" height="32" viewBox="0 0 30 32"><path d="M10 2h10l-3 6h-4z" fill="#fff"/><ellipse cx="15" cy="20" rx="13" ry="11" fill="#fff"/><text x="15" y="26" font-family="Lato,sans-serif" font-weight="900" font-size="15" fill="#d4553a" text-anchor="middle">$</text></svg>
            <h4>INVESTMENT</h4>
          </div>
          <ul><li>WE PAY MOST CLOSING COSTS</li><li>THEY INHERITED ANOTHER HOME</li><li>THEY HAVE FALLEN BEHIND ON THEIR PAYMENTS</li></ul>
        </div>
      </div>
    </div>
  </section>

  <section class="contact wrap">
    <div class="mark"></div>
    <h2 class="section-title">CONTACT</h2>
    <p class="sub">Have a question or a house to sell? Send us a note and we will reply soon.</p>
    <div class="form">
      <div class="col">
        <div class="field"><span class="ico"></span>Enter Name</div>
        <div class="field"><span class="ico"></span>Enter Email</div>
        <div class="field"><span class="ico"></span>Enter Phone</div>
      </div>
      <div class="col">
        <div class="field message"><span class="ico"></span>Enter Message</div>
      </div>
    </div>
    <span class="btn">SEND</span>
  </section>

  <footer class="footer">
    <div class="wrap">
      <div class="fcol">
        <h5>MAIN MENU</h5>
        <ul><li>Home</li><li>About Us</li><li>FAQ</li><li>Contact Us</li><li>Testimonials</li><li>Houses To Buy</li></ul>
      </div>
      <div class="fcol">
        <h5>QUICK LINKS</h5>
        <ul><li>Customer Policy</li><li>Pro Policy</li><li>Terms and conditions of use</li><li>Secure payment</li><li>Site map</li></ul>
      </div>
      <div class="fcol">
        <h5>SERVICES</h5>
        <p>Buy houses for cash</p>
        <h5 style="margin-top:14px;margin-bottom:4px">FOLLOW US ON</h5>
        <div class="social"><span></span><span></span><span></span><span></span><span></span></div>
      </div>
      <div class="fcol">
        <h5>NEWSLETTER</h5>
        <p>Lorem ipsum dolor sit amet</p>
        <div class="nl-input">Your name</div>
        <div class="nl-input">Email</div>
        <span class="nl-btn">SUBMIT</span>
      </div>
    </div>
  </footer>
  <div class="copyright">Copyright © 2016 DORLIT HOMES. All Rights Reserved.</div>
</div>
</body>
</html>
```